kestrova business cards

Hey design gurus!
I'm after a clean, modern, stylish business card for my about to be launched company.
I've uploaded the logos for my company "Kestrova Electrical Solutions"
and also the tarrow alliance logo to whom i am associated.

```html
<!DOCTYPE html>
<html lang="en">
<head>
<meta charset="utf-8">
<title>Kestrova Electrical Solutions – Business Cards</title>
<link rel="stylesheet" href="https://fonts.googleapis.com/css2?family=Lato:wght@400;700;900&display=swap">
<style>
  :root {
    --stage: #2b2b2d;
    --card-white: #ffffff;
    --card-navy: #0b1520;
    --brand-blue: #0a79c6;
    --ink: #0b1520;
    --text-light: #f2f4f6;
    --badge-line: #c9d1d8;
  }
  * { box-sizing: border-box; margin: 0; padding: 0; }
  html, body { width: 1200px; height: 875px; overflow: hidden; }
  body {
    background: var(--stage);
    font-family: "Lato", sans-serif;
    display: flex;
    flex-direction: column;
    align-items: center;
    justify-content: center;
    gap: 28px;
  }
  .card {
    width: 700px;
    height: 400px;
    border-radius: 22px;
    position: relative;
    overflow: hidden;
  }
  /* Front */
  .card--front {
    background: var(--card-white);
    display: flex;
    align-items: center;
    justify-content: center;
  }
  .front-brand {
    display: flex;
    align-items: center;
    gap: 18px;
  }
  .brand-dot {
    width: 34px; height: 34px;
    border-radius: 50%;
    background: var(--brand-blue);
    flex: none;
  }
  .front-brand__name {
    font-weight: 900;
    color: var(--brand-blue);
    font-size: 38px;
    line-height: 1.05;
    letter-spacing: 1px;
    text-transform: uppercase;
  }
  /* Back */
  .card--back { background: var(--card-navy); }
  .back-panel { position: absolute; inset: 0; }
  .back-brand {
    position: absolute;
    left: 40px; top: 0; bottom: 0;
    width: 260px;
    display: flex;
    align-items: center;
    justify-content: center;
    text-align: center;
  }
  .back-brand__name {
    font-weight: 900;
    color: var(--ink);
    font-size: 34px;
    letter-spacing: 1px;
    text-transform: uppercase;
  }
  .contact {
    position: absolute;
    right: 40px; top: 38px;
    text-align: right;
    color: var(--text-light);
  }
  .contact__name {
    font-weight: 900;
    color: var(--brand-blue);
    font-size: 30px;
    text-transform: uppercase;
    letter-spacing: 0.5px;
  }
  .contact__role {
    font-weight: 700;
    font-size: 17px;
    margin-top: 2px;
    margin-bottom: 18px;
  }
  .contact__list { list-style: none; }
  .contact__item {
    display: flex;
    justify-content: flex-end;
    align-items: center;
    gap: 10px;
    font-size: 15px;
    line-height: 22px;
  }
  .contact__item svg { width: 13px; height: 13px; flex: none; }
  .contact__gap { margin-top: 8px; }
  .partner-badge {
    position: absolute;
    right: 40px; bottom: 34px;
    width: 150px; height: 44px;
    border: 1.5px solid var(--badge-line);
    border-radius: 5px;
  }
</style>
</head>
<body>

<section class="card card--front" aria-label="Business card front">
  <div class="front-brand">
    <span class="brand-dot"></span>
    <span class="front-brand__name">Kestrova<br>Electrical Solutions</span>
  </div>
</section>

<section class="card card--back" aria-label="Business card back">
  <svg class="back-panel" viewBox="0 0 700 400" aria-hidden="true">
    <path d="M0 0 H250 C330 10 380 80 380 170 C380 270 320 330 250 350 C220 360 200 400 200 400 H0 Z" fill="#ffffff"/>
  </svg>

  <div class="back-brand">
    <span class="back-brand__name">Kestrova</span>
  </div>

  <div class="contact">
    <div class="contact__name">Dorian Welles</div>
    <div class="contact__role">Founder &amp; CEO</div>
    <ul class="contact__list">
      <li class="contact__item">48 Larkfield Road, Halden
        <svg viewBox="0 0 12 12"><path d="M6 0.5a4 4 0 0 0-4 4c0 3 4 7 4 7s4-4 4-7a4 4 0 0 0-4-4z" fill="#0a79c6"/><circle cx="6" cy="4.5" r="1.5" fill="#0b1520"/></svg></li>
      <li class="contact__item">Westmark, Norvale, 40215
        <svg viewBox="0 0 12 12"></svg></li>
      <li class="contact__item contact__gap">(555) 014-2290
        <svg viewBox="0 0 12 12"><path d="M2.5 1h2l1 2.5-1.3 1a6.5 6.5 0 0 0 3.3 3.3l1-1.3 2.5 1v2A1.5 1.5 0 0 1 9.5 11 8.5 8.5 0 0 1 1 2.5 1.5 1.5 0 0 1 2.5 1z" fill="#0a79c6"/></svg></li>
      <li class="contact__item">(555) 014-3381
        <svg viewBox="0 0 12 12"><rect x="3" y="0.5" width="6" height="11" rx="1.2" fill="none" stroke="#0a79c6" stroke-width="1.3"/></svg></li>
      <li class="contact__item">(555) 014-4472
        <svg viewBox="0 0 12 12"><rect x="1" y="4" width="10" height="5" rx="1" fill="#0a79c6"/><rect x="3" y="1" width="6" height="3" fill="#0a79c6"/><rect x="3" y="8" width="6" height="3" fill="#0a79c6"/></svg></li>
      <li class="contact__item contact__gap">office@kestrova-example.com
        <svg viewBox="0 0 12 12"><rect x="0.5" y="2" width="11" height="8" rx="1" fill="#0a79c6"/><path d="M1 2.5l5 4 5-4" fill="none" stroke="#0b1520" stroke-width="1"/></svg></li>
      <li class="contact__item">www.kestrova-example.com
        <svg viewBox="0 0 12 12"><circle cx="6" cy="6" r="5" fill="none" stroke="#0a79c6" stroke-width="1.3"/><path d="M1 6h10M6 1c-2 2.5-2 7.5 0 10M6 1c2 2.5 2 7.5 0 10" fill="none" stroke="#0a79c6" stroke-width="1"/></svg></li>
    </ul>
  </div>

  <div class="partner-badge" role="img" aria-label="Tarrow Alliance partner badge"></div>
</section>

</body>
</html>
```